Grand Opening for Brightvale Church

Would like to have a BillBoard Created according to the specs listed by the company who will be producing the print. I am attaching the spec sheet to this post. I am also attaching a couple different picture options as well as a former Billboard design that was done. I would like the design to incorporate my logo, picture. I am okay if the background on the picture is eliminated for creative purposes. The words to be displayed is "Grand Opening" April 12, 2020 at the former Harlan Middle School) 41st Copper Lake Rd.

Colors

Designer to choose colors to be used in the design.

Requirements
Must have
• Something that pops
Nice to have
• Good color coordinations and clearly visible text

```html
<!DOCTYPE html>
<html lang="en">
<head>
<meta charset="utf-8">
<title>Brightvale Church — Grand Opening Billboard</title>
<link href="https://fonts.googleapis.com/css2?family=Exo+2:wght@600&family=Roboto+Condensed:wght@700&display=swap" rel="stylesheet">
<style>
  :root {
    --page-bg: #e9e9ea;
    --board-black: #050505;
    --stage-brown: #3a2418;
    --stage-warm: #6b3c22;
    --gold: #eda63a;
    --yellow: #f6d437;
    --orange: #f0982c;
    --white: #ffffff;
  }
  * { margin: 0; padding: 0; box-sizing: border-box; }
  html, body {
    width: 1200px;
    height: 680px;
    overflow: hidden;
    background: var(--page-bg);
  }
  .billboard {
    position: absolute;
    left: 118px;
    top: 112px;
    width: 962px;
    height: 450px;
    background: var(--board-black);
    overflow: hidden;
  }
  .speaker-photo {
    position: absolute;
    right: 0;
    top: 0;
    width: 440px;
    height: 100%;
    background:
      radial-gradient(ellipse 40% 55% at 62% 55%, var(--stage-warm) 0%, rgba(107,60,34,0) 70%),
      linear-gradient(90deg, var(--board-black) 0%, var(--stage-brown) 35%, #241510 100%);
  }
  .brand {
    position: absolute;
    left: 72px;
    top: 118px;
    width: 272px;
    display: flex;
    align-items: center;
    gap: 12px;
  }
  .brand-dot {
    width: 22px;
    height: 22px;
    border-radius: 50%;
    background: var(--orange);
    flex: none;
  }
  .brand-name {
    font-family: "Exo 2", sans-serif;
    font-weight: 600;
    font-size: 30px;
    line-height: 1.1;
    color: var(--white);
  }
  .divider {
    position: absolute;
    left: 362px;
    top: 86px;
    width: 1px;
    height: 138px;
    background: linear-gradient(180deg, rgba(237,166,58,0) 0%, var(--gold) 50%, rgba(237,166,58,0) 100%);
  }
  .headline {
    position: absolute;
    left: 390px;
    top: 112px;
    font-family: "Exo 2", sans-serif;
    font-weight: 600;
    font-size: 40px;
    line-height: 46px;
    letter-spacing: 0.5px;
  }
  .headline .line-one { display: block; color: var(--gold); }
  .headline .line-two { display: block; color: var(--yellow); }
  .event-date {
    position: absolute;
    left: 170px;
    top: 258px;
    width: 376px;
    height: 74px;
    border: 2px solid var(--orange);
    display: flex;
    align-items: center;
    justify-content: center;
    font-family: "Roboto Condensed", sans-serif;
    font-weight: 700;
    font-size: 42px;
    color: var(--orange);
    letter-spacing: 1px;
  }
  .venue {
    position: absolute;
    left: 158px;
    top: 350px;
    width: 400px;
    text-align: center;
    font-family: "Roboto Condensed", sans-serif;
    font-weight: 700;
    font-size: 17px;
    color: var(--white);
  }
  .venue sup { font-size: 10px; }
</style>
</head>
<body>
  <main class="billboard">
    <div class="speaker-photo" role="img" aria-label="Pastor in a brown corduroy jacket speaking on a dimly lit stage, hands open toward the audience"></div>

    <div class="brand">
      <span class="brand-dot"></span>
      <span class="brand-name">Brightvale Church</span>
    </div>

    <div class="divider"></div>

    <h1 class="headline">
      <span class="line-one">GRAND</span>
      <span class="line-two">OPENING</span>
    </h1>

    <p class="event-date">APRIL 12, 2020</p>

    <p class="venue">Former Harlan Middle School, 41<sup>st</sup> Copper Lake Rd.</p>
  </main>
</body>
</html>
```